New Stationary and Logo Design for Start Up Company

We need a logo design and stationary set including letterhead, business card (double sided), compliments slip and envelope for a new company Bright Lantern Media.
The files should be editable to update address and standard contact details, will need to forward to web designer and stationary printer.
The company will be an online marketer and distributer of various business education products in Australia.
The designs should convey simple clean image
Target Market(s)
Small business owners and professional service providers (ie Accountants, Lawyers, Real Estate Agents) in Australia
Industry/Entity Type
Education
Look and feel
Each slider illustrates characteristics of the customer's brand and the style your logo design should communicate.

```html
<!DOCTYPE html>
<html lang="en">
<head>
<meta charset="utf-8">
<title>Bright Lantern Media – Stationery Set</title>
<link rel="stylesheet" href="https://fonts.googleapis.com/css2?family=Source+Sans+3:wght@400&family=Montserrat:wght@400;800&display=swap">
<style>
  :root {
    --navy: #263674;
    --red: #d2232a;
    --ink: #1a1a1a;
    --paper: #ffffff;
    --edge: #6b6b6b;
    --shadow: rgba(0, 0, 0, 0.35);
  }
  html, body { margin: 0; padding: 0; overflow: hidden; }
  body { background: var(--paper); }
  .canvas {
    position: relative; width: 1200px; height: 900px; overflow: hidden;
    background: var(--paper);
    font-family: "Montserrat", Arial, sans-serif;
  }
  .sheet {
    position: absolute; background: var(--paper);
    border: 1px solid var(--edge);
    box-shadow: 5px 5px 6px var(--shadow);
    overflow: hidden; box-sizing: border-box;
  }
  .sheet svg.band { position: absolute; inset: 0; width: 100%; height: 100%; }
  .wordmark {
    position: absolute; margin: 0; color: var(--navy);
    font-family: "Source Sans 3", Arial, sans-serif; font-weight: 400;
    white-space: nowrap; line-height: 1;
  }
  .person {
    position: absolute; margin: 0; color: var(--red);
    font-weight: 800; letter-spacing: 0.22em; white-space: nowrap; line-height: 1;
  }
  .details {
    position: absolute; margin: 0; color: var(--ink);
    font-weight: 800; letter-spacing: 0.14em; white-space: nowrap;
  }
  .rule { position: absolute; background: var(--red); }

  /* Letterhead */
  .letterhead { left: 44px; top: 70px; width: 541px; height: 766px; }
  .letterhead .wordmark { left: 38px; top: 62px; font-size: 15.5px; }
  .letterhead .rule.top { left: 355px; top: -1px; width: 7px; height: 96px; }
  .letterhead .rule.bottom { left: 355px; top: 682px; width: 7px; height: 84px; }
  .letterhead .person { left: 377px; top: 18px; font-size: 10px; }
  .letterhead .details { left: 392px; font-size: 8px; line-height: 13.5px; }
  .letterhead .details.contact { top: 37px; }
  .letterhead .details.address { top: 701px; }

  /* Business cards */
  .card-front { left: 651px; top: 56px; width: 229px; height: 131px; }
  .card-front .wordmark { left: 0; right: 0; top: 58px; text-align: center; font-size: 11.5px; }
  .card-back { left: 898px; top: 58px; width: 229px; height: 131px; background: var(--navy); border-color: var(--navy); }
  .card-back .details { color: var(--paper); font-size: 7px; line-height: 11.7px; top: 34px; }
  .card-back .details.contact { right: 115px; text-align: right; }
  .card-back .details.address { left: 126px; }
  .card-back .person { left: 0; right: 0; text-align: center; top: 114px; font-size: 8px; }

  /* Compliments slip */
  .compliments { left: 620px; top: 268px; width: 557px; height: 273px; }
  .compliments .greeting {
    position: absolute; left: 43px; top: 54px; margin: 0; color: var(--red);
    font-weight: 400; font-size: 21px; letter-spacing: 0.09em; white-space: nowrap;
  }
  .compliments .wordmark { right: 24px; top: 60px; font-size: 19px; }
  .compliments .person { right: 24px; top: 166px; font-size: 10px; }
  .compliments .details { right: 24px; text-align: right; font-size: 7.5px; line-height: 11.5px; }
  .compliments .details.contact { top: 183px; }
  .compliments .details.address { top: 222px; }

  /* Envelope */
  .envelope { left: 612px; top: 569px; width: 557px; height: 139px; border-color: #e4e4e4; }
  .envelope .wordmark { left: 9px; top: 82px; font-size: 19px; }
  .envelope .divider {
    position: absolute; top: 10px; width: 4px; height: 118px;
    background: linear-gradient(to bottom, rgba(210,35,42,0), rgba(210,35,42,0.75) 50%, rgba(210,35,42,0));
  }
  .envelope .divider.first { left: 259px; }
  .envelope .divider.second { left: 417px; }
  .envelope .person { left: 272px; top: 66px; font-size: 13px; letter-spacing: 0.12em; }
  .envelope .details { left: 427px; font-size: 9px; line-height: 14.5px; }
  .envelope .details.contact { top: 30px; }
  .envelope .details.address { top: 80px; }

  /* Master logo */
  .master-logo { left: 645px; top: 812px; font-size: 43px; letter-spacing: 0.01em; }
</style>
</head>
<body>
<main class="canvas">

  <section class="sheet letterhead" aria-label="Letterhead">
    <svg class="band" viewBox="0 0 541 766" preserveAspectRatio="none" aria-hidden="true">
      <polygon points="541,175 455,397 541,623" fill="var(--navy)"/>
    </svg>
    <h1 class="wordmark">BRIGHT LANTERN MEDIA</h1>
    <div class="rule top"></div>
    <p class="person">Daniel Harte</p>
    <p class="details contact">hello@lantern.au<br>www.lantern.com.au<br>0298765432</p>
    <div class="rule bottom"></div>
    <p class="details address">42 Harbourlane<br>Northbridge<br>Australia</p>
  </section>

  <section class="sheet card-front" aria-label="Business card front">
    <svg class="band" viewBox="0 0 229 131" preserveAspectRatio="none" aria-hidden="true">
      <polygon points="0,131 115,84 229,131" fill="var(--navy)"/>
    </svg>
    <p class="wordmark">BRIGHT LANTERN MEDIA</p>
  </section>

  <section class="sheet card-back" aria-label="Business card back">
    <svg class="band" viewBox="0 0 229 131" preserveAspectRatio="none" aria-hidden="true">
      <polygon points="0,131 115,85 229,131" fill="var(--paper)"/>
    </svg>
    <p class="details contact">0298765432<br>www.lantern.com.au<br>hello@lantern.au</p>
    <p class="details address">42 Harbourlane<br>Northbridge<br>Australia</p>
    <p class="person">Daniel Harte</p>
  </section>

  <section class="sheet compliments" aria-label="Compliments slip">
    <svg class="band" viewBox="0 0 557 273" preserveAspectRatio="none" aria-hidden="true">
      <polygon points="0,0 52,137 0,273" fill="var(--navy)"/>
    </svg>
    <p class="greeting">with compliments</p>
    <p class="wordmark">BRIGHT LANTERN MEDIA</p>
    <p class="person">Daniel Harte</p>
    <p class="details contact">hello@lantern.au<br>www.lantern.com.au<br>0298765432</p>
    <p class="details address">42 Harbourlane<br>Northbridge<br>Australia</p>
  </section>

  <section class="sheet envelope" aria-label="Envelope">
    <p class="wordmark">BRIGHT LANTERN MEDIA</p>
    <div class="divider first"></div>
    <p class="person">Daniel Harte</p>
    <div class="divider second"></div>
    <p class="details contact">hello@lantern.au<br>www.lantern.com.au<br>0298765432</p>
    <p class="details address">42 Harbourlane<br>Northbridge<br>Australia</p>
  </section>

  <p class="wordmark master-logo">BRIGHT LANTERN MEDIA</p>

</main>
</body>
</html>
```